Buisness card

**Front Side:**

**[Your Company Logo]**
**Steadfast Upkeep Engineering**
*Keeping Your Equipment Running Smoothly*

**Contact Information:**
- **Name:** [dale Harwick
- **Title:** [owner
- **Phone:** [5073918246
- **Email:** dale@suevx.com

**Back Side:**

**Services Offered:**
- Routine Inspections
- Equipment Maintenance
- Emergency Repairs
- Consultation Services
- New installs
Tag line
Be proactive not reactive

```html
<!DOCTYPE html>
<html lang="en">
<head>
<meta charset="utf-8">
<title>Steadfast Upkeep Engineering – Business Card</title>
<link href="https://fonts.googleapis.com/css2?family=Arimo:wght@400;700&display=swap" rel="stylesheet">
<style>
  :root {
    --page-bg: #e4e4e4;
    --card-front: #ffffff;
    --card-back: #323232;
    --navy: #0d2b74;
    --accent-blue: #1a66e0;
    --text-grey: #555555;
    --divider: #b8b8b8;
    --white: #ffffff;
  }
  * { margin: 0; padding: 0; box-sizing: border-box; }
  html, body {
    width: 1200px; height: 1200px; overflow: hidden;
    background: var(--page-bg);
    font-family: "Arimo", Arial, sans-serif;
  }
  .card {
    position: absolute;
    left: 267px;
    width: 690px;
    height: 394px;
  }
  .card--front { top: 158px; background: var(--card-front); }
  .card--back  { top: 653px; background: var(--card-back); }

  /* Front: brand block */
  .brand {
    position: absolute; left: 88px; top: 170px;
    display: flex; align-items: center; gap: 10px;
  }
  .brand__mark {
    width: 52px; height: 52px; border-radius: 50%;
    background: var(--navy); flex: none;
  }
  .brand__name {
    font-size: 13.5px; font-weight: 700; color: var(--navy);
    line-height: 1.2; white-space: nowrap;
  }
  .brand__motto {
    font-size: 10px; font-weight: 700; color: var(--navy);
    letter-spacing: 0.2px; margin-top: 3px; white-space: nowrap;
  }
  .divider {
    position: absolute; left: 370px; top: 124px;
    width: 2px; height: 145px; background: var(--divider);
  }
  .person { position: absolute; left: 395px; top: 120px; }
  .person__name {
    font-size: 27px; font-weight: 700; color: var(--navy); line-height: 1.1;
  }
  .person__title {
    font-size: 15px; color: var(--text-grey); margin-top: 2px;
  }
  .contacts { list-style: none; margin-top: 30px; }
  .contacts li {
    display: flex; align-items: center; gap: 12px;
    font-size: 16.5px; color: var(--text-grey); height: 21px;
  }
  .contacts svg { width: 15px; height: 15px; flex: none; fill: var(--accent-blue); }

  /* Back */
  .back__mark {
    position: absolute; left: 290px; top: 130px;
    width: 110px; height: 110px; border-radius: 50%;
    background: var(--white);
  }
  .back__name {
    position: absolute; left: 0; right: 0; top: 262px;
    text-align: center; color: var(--white);
    font-size: 15px; font-weight: 700; letter-spacing: 0.3px;
  }
  .back__slogan {
    position: absolute; left: 0; right: 0; top: 324px;
    text-align: center; color: var(--white); font-size: 17.5px;
  }
</style>
</head>
<body>
  <section class="card card--front">
    <div class="brand">
      <div class="brand__mark"></div>
      <div>
        <div class="brand__name">Steadfast Upkeep Engineering</div>
        <div class="brand__motto">BE PROACTIVE NOT REACTIVE</div>
      </div>
    </div>
    <div class="divider"></div>
    <div class="person">
      <div class="person__name">Dale Harwick</div>
      <div class="person__title">Owner</div>
      <ul class="contacts">
        <li>
          <svg viewBox="0 0 16 16" aria-hidden="true"><path d="M3.6 1.2l2.3 2.6-1.3 2c.9 2 2.5 3.6 4.5 4.6l2-1.3 2.6 2.3-1.3 2.2C7.6 13.3 2.7 8.4 1.4 2.5z"/></svg>
          5073918246
        </li>
        <li>
          <svg viewBox="0 0 16 16" aria-hidden="true"><path d="M1 3.5h14v9H1z M2 4.6v.4l6 4 6-4v-.4z" fill-rule="evenodd"/></svg>
          dale@suevx.com
        </li>
        <li>
          <svg viewBox="0 0 16 16" aria-hidden="true"><circle cx="8" cy="8" r="7"/><path d="M5 4.5c1.2.3 1.8 1.3 1.4 2.4-.4 1-1.6 1-1.8 2.3M10.5 9c.8.6.6 2-.3 2.8" stroke="#fff" stroke-width="1.2" fill="none"/></svg>
          www.suevx.com
        </li>
      </ul>
    </div>
  </section>

  <section class="card card--back">
    <div class="back__mark"></div>
    <div class="back__name">Steadfast Upkeep Engineering</div>
    <div class="back__slogan">Keeping Your Equipment Running Smoothly*</div>
  </section>
</body>
</html>
```